Cleaning services Business Card Design

I need a business card design for my Cleaning business. I would like perhaps emphasis on the company name, Muddle to Marvel. Maybe the Muddle would to dirty and the marvel would have sprinkles.

Industry/Entity Type

Business

Contact Information for Business Card

Muddle to Marvel Cleaning Services, Teodoro Perlas, Industrial, Commercial, & Residential 418-635-0247

```html
<!DOCTYPE html>
<html lang="en">
<head>
<meta charset="utf-8">
<title>Muddle to Marvel Cleaning Services – Business Cards</title>
<link rel="stylesheet" href="https://fonts.googleapis.com/css2?family=Lato:wght@400;700&display=swap">
<style>
  :root {
    --page-bg: #4a423d;
    --card-bg: #0c0c0c;
    --brand-blue: #2f5ff0;
    --brand-green: #8cc21a;
    --text-white: #f2f2f2;
    --brand-grey: #7a7a7a;
  }
  * { margin: 0; padding: 0; box-sizing: border-box; }
  html, body {
    width: 1200px;
    height: 844px;
    overflow: hidden;
    background: var(--page-bg);
    font-family: "Lato", sans-serif;
  }
  .card-sheet {
    position: absolute;
    inset: 0;
    display: flex;
    align-items: center;
    justify-content: center;
    gap: 40px;
  }
  .card {
    position: relative;
    width: 520px;
    height: 297px;
    background: var(--card-bg);
    box-shadow: 0 14px 30px rgba(0,0,0,0.45);
    overflow: hidden;
  }

  /* Brand lockup */
  .brand {
    position: absolute;
    display: flex;
    align-items: center;
    gap: 14px;
  }
  .brand-square {
    width: 58px;
    height: 58px;
    flex: none;
  }
  .brand-name {
    font-weight: 400;
    font-size: 24px;
    line-height: 1.15;
    letter-spacing: 0.5px;
  }
  .brand-name span { display: block; }
  .brand-name .brand-sub { letter-spacing: 3px; }

  /* Front */
  .card-front .brand { left: 44px; top: 98px; }
  .card-front .brand-square { background: var(--brand-blue); }
  .card-front .brand-name { color: var(--brand-blue); }

  .contact {
    position: absolute;
    right: 40px;
    top: 176px;
    text-align: right;
  }
  .contact-name {
    color: var(--brand-green);
    font-weight: 700;
    font-size: 17px;
    margin-bottom: 8px;
  }
  .contact-phone {
    color: var(--text-white);
    font-size: 14px;
    display: flex;
    align-items: center;
    justify-content: flex-end;
    gap: 6px;
  }
  .contact-phone svg { width: 12px; height: 12px; }

  /* Back */
  .card-back .brand { left: 118px; top: 84px; }
  .card-back .brand-square { background: var(--brand-grey); }
  .card-back .brand-name { color: var(--brand-grey); }

  .rule {
    position: absolute;
    height: 1px;
    background: var(--brand-green);
  }
  .rule-upper { right: 0; top: 162px; width: 110px; }
  .rule-lower { left: 0; top: 224px; width: 150px; }
  .tagline {
    position: absolute;
    left: 160px;
    top: 214px;
    color: var(--brand-green);
    font-weight: 700;
    font-size: 13px;
    letter-spacing: 0.3px;
  }
</style>
</head>
<body>
  <main class="card-sheet">
    <section class="card card-front" aria-label="Business card front">
      <div class="brand">
        <div class="brand-square"></div>
        <div class="brand-name">
          <span>MUDDLE TO MARVEL</span>
          <span class="brand-sub">Cleaning Services</span>
        </div>
      </div>
      <div class="contact">
        <p class="contact-name">Teodoro Perlas</p>
        <p class="contact-phone">418-635-0247
          <svg viewBox="0 0 24 24" aria-hidden="true"><path fill="var(--brand-green)" d="M6.6 10.8a15.2 15.2 0 0 0 6.6 6.6l2.2-2.2a1 1 0 0 1 1-.25 11.4 11.4 0 0 0 3.6.57 1 1 0 0 1 1 1V20a1 1 0 0 1-1 1A17 17 0 0 1 3 4a1 1 0 0 1 1-1h3.5a1 1 0 0 1 1 1c0 1.25.2 2.45.57 3.57a1 1 0 0 1-.25 1z"/></svg>
        </p>
      </div>
    </section>

    <section class="card card-back" aria-label="Business card back">
      <div class="brand">
        <div class="brand-square"></div>
        <div class="brand-name">
          <span>MUDDLE TO MARVEL</span>
          <span class="brand-sub">Cleaning Services</span>
        </div>
      </div>
      <div class="rule rule-upper"></div>
      <p class="tagline">Industrial, Commercial &amp; Residential</p>
      <div class="rule rule-lower"></div>
    </section>
  </main>
</body>
</html>
```